buseisness card

design a card that similar to my web site
TRELLINGWORKSLLC .COM

Contact Information for Business Card

NAME PHONE # WEBSITE EMAIL AND DISCTIPTION OF WHAT WE DO

Colors
0054AA
0677BA
7BADD7
CADEEF
E8F1F8

Requirements
Must have
• lOGO AND DETAILS
Nice to have
• I LIKE THE WATER LIKE ON MY WEB SITE

```html
<!DOCTYPE html>
<html lang="en">
<head>
<meta charset="utf-8">
<title>Trelling Works – Business Card</title>
<link rel="stylesheet" href="https://fonts.googleapis.com/css2?family=Open+Sans:wght@400;600;700&display=swap">
<style>
  :root {
    --stage: #cccccc;
    --deep: #0054AA;
    --brand: #0677BA;
    --bright: #1d9be2;
    --sky: #7BADD7;
    --mist: #CADEEF;
    --pale: #E8F1F8;
    --eco: #4cc26a;
    --ink: #333333;
    --muted: #555b61;
    --white: #ffffff;
  }
  * { box-sizing: border-box; margin: 0; padding: 0; }
  html, body {
    width: 1200px; height: 800px; overflow: hidden;
    background: var(--stage);
    font-family: "Open Sans", sans-serif;
  }
  .card {
    position: absolute; top: 290px;
    width: 402px; height: 230px; overflow: hidden;
  }
  .card--front { left: 174px; color: var(--white); text-align: center; }
  .card--back { left: 631px; background: var(--white); }

  .water {
    position: absolute; inset: 0;
    background:
      radial-gradient(ellipse 70% 35% at 50% 0%, rgba(120,150,160,0.45), transparent 70%),
      linear-gradient(180deg, #1d4a58 0%, #17566a 30%, #0f4a5e 60%, #082c3b 100%);
  }
  .front-content { position: relative; }
  .brand-mark {
    position: absolute; left: 50%; top: 24px; transform: translateX(-50%);
    width: 26px; height: 26px; border-radius: 50%; background: var(--white);
  }
  .brand-name {
    position: absolute; left: 0; right: 0; top: 73px;
    font-size: 12.5px; font-weight: 600; letter-spacing: 0.2px;
  }
  .headline {
    position: absolute; left: 0; right: 0; top: 107px;
    font-size: 16.5px; font-weight: 700; color: var(--bright); letter-spacing: 0.1px;
  }
  .systems {
    position: absolute; left: 0; right: 0; top: 128px;
    font-size: 10.5px; font-weight: 600;
  }
  .systems .hl { color: var(--bright); }
  .eco-line {
    position: absolute; left: 0; right: 0; top: 151px;
    font-size: 8.6px; font-weight: 600; line-height: 11.5px;
  }
  .eco-line .eco { color: var(--eco); }
  .site {
    position: absolute; left: 0; right: 0; top: 190px;
    font-size: 8.6px; color: var(--bright);
  }

  .back-mark {
    position: absolute; left: 224px; top: 52px;
    width: 150px; height: 150px; border-radius: 50%; background: var(--pale);
  }
  .person { position: absolute; left: 34px; top: 40px; }
  .person-name { font-size: 19px; font-weight: 600; color: var(--brand); line-height: 24px; }
  .person-role { font-size: 12.5px; color: var(--ink); line-height: 18px; }
  .contacts {
    position: absolute; left: 32px; top: 136px; list-style: none;
    font-size: 12.5px; color: var(--muted); line-height: 17.6px;
  }
  .contacts li { display: flex; align-items: center; gap: 6px; }
  .contacts svg { width: 10px; height: 10px; flex: none; }
</style>
</head>
<body>
  <section class="card card--front">
    <div class="water" role="img" aria-label="Underwater photograph of deep blue-teal sea with light rippling on the surface"></div>
    <div class="front-content">
      <span class="brand-mark"></span>
      <p class="brand-name">TRELLING WORKS</p>
      <h1 class="headline">FOAM PROPORTIONER TESTING</h1>
      <p class="systems"><span class="hl">HEF</span>, <span class="hl">AR</span>, AND <span class="hl">AFFF</span> SYSTEM</p>
      <p class="eco-line">AN <span class="eco">ECO</span> FRIENDLY COMPANY DOING<br><span class="eco">ECO</span> FRIENDLY TESTING</p>
      <p class="site">www.trellingworksllc.com</p>
    </div>
  </section>

  <section class="card card--back">
    <span class="back-mark"></span>
    <div class="person">
      <h2 class="person-name">Your Name</h2>
      <p class="person-role">Director</p>
    </div>
    <ul class="contacts">
      <li>
        <svg viewBox="0 0 10 10"><rect x="2.5" y="0.5" width="5" height="9" rx="1" fill="none" stroke="var(--brand)" stroke-width="1"/></svg>
        <span>0044 555 019</span>
      </li>
      <li>
        <svg viewBox="0 0 10 10"><path d="M9.5 0.5 L0.5 4.5 L4 5.8 L5.2 9.5 Z M9.5 0.5 L4 5.8" fill="none" stroke="var(--brand)" stroke-width="0.9" stroke-linejoin="round"/></svg>
        <span>name@trellingworksllc.com</span>
      </li>
      <li>
        <svg viewBox="0 0 10 10" fill="none" stroke="var(--brand)" stroke-width="0.9"><circle cx="5" cy="5" r="4.3"/><ellipse cx="5" cy="5" rx="1.9" ry="4.3"/><path d="M0.7 5 H9.3"/></svg>
        <span>trellingworksllc.com</span>
      </li>
    </ul>
  </section>
</body>
</html>
```